Towing Company Website Towing Bergfeld Ost

Hello I need a cool website for my towing company. - Home - About us - Parking Enforcement - Repossession - Disaster Recovery - Accident Recovery - Contact So someone would have to install the website on Hostarly for me. No idea how that works.

Target Market(s)

www.bergungsfix.cc

Contact Information for Business Card

Bergungsfix Talwiesen Ost
P: 044 736 48 91
F: 044 736 48 97
E: mail@bergungsfix.cc
W: www.bergungsfix.cc

Lukas Vontobel
M: 075 628 94 17

Number of Pages Required

5+ page

Font styles to use
Sans Serif

Colors

Designer to choose colors to be used in the design.

```html
<!DOCTYPE html>
<html lang="en">
<head>
<meta charset="utf-8">
<title>Bergungsfix Talwiesen Ost – Towing Bergfeld Ost</title>
<link href="https://fonts.googleapis.com/css2?family=Bree+Serif&family=Roboto:wght@400;500;700;900&display=swap" rel="stylesheet">
<style>
:root{
  --red:#e30613;
  --red-dark:#c10510;
  --ink:#1d1d1d;
  --dark:#1b1b1b;
  --dark-2:#262626;
  --grey:#6b6b6b;
  --light:#ececec;
  --white:#ffffff;
}
*{box-sizing:border-box;margin:0;padding:0}
html,body{width:1200px;height:4296px;overflow:hidden;background:var(--white)}
body{font-family:"Roboto",Arial,sans-serif;color:var(--ink);position:relative}
.abs{position:absolute}
.slab{font-family:"Bree Serif",Georgia,serif;font-weight:400}
.btn{position:absolute;display:flex;align-items:center;justify-content:center;gap:8px;border-radius:22px;font-size:12px;font-weight:700;color:var(--white);text-transform:uppercase;letter-spacing:.3px}
.btn-red{background:var(--red)}
.btn-dark{background:#2b2b2b}
.btn-ghost{border:2px solid var(--white)}
.arrow{width:14px;height:14px;border-radius:50%;background:var(--white);display:inline-flex;align-items:center;justify-content:center}
.arrow::after{content:"";border-left:5px solid var(--red);border-top:3.5px solid transparent;border-bottom:3.5px solid transparent;margin-left:2px}
.btn-dark .arrow::after{border-left-color:#2b2b2b}
.heading{position:absolute;font-size:31px;line-height:1}
.heading::before{content:"";position:absolute;left:0;bottom:-10px;width:44px;height:3px;background:var(--red)}
.lead{position:absolute;font-size:14px;font-weight:700}
.copy{position:absolute;font-size:12.5px;line-height:25px;color:var(--grey)}
.vertical{position:absolute;font-weight:900;color:#ebebeb;transform:rotate(-90deg);transform-origin:center;white-space:nowrap;letter-spacing:2px}
.ghost-word{position:absolute;font-weight:900;white-space:nowrap;letter-spacing:2px;line-height:1}
.site-header{position:absolute;left:0;top:0;width:1200px;height:100px;background:var(--white)}
.brand{position:absolute;left:143px;top:18px;display:flex;align-items:center;gap:10px}
.brand-square{width:16px;height:16px;background:var(--red)}
.brand-name{font-family:"Bree Serif",serif;font-size:22px;line-height:24px;color:var(--ink)}
.call{position:absolute;right:140px;top:30px;display:flex;align-items:center;gap:12px;font-weight:700;font-size:20px;color:var(--red)}
.nav{position:absolute;left:0;top:100px;width:1200px;height:43px;background:var(--red);display:flex;align-items:center;padding:0 143px;gap:31px}
.nav a{color:var(--white);font-size:13px;font-weight:500;text-decoration:none;text-transform:uppercase}
.hero{position:absolute;left:0;top:143px;width:1200px;height:632px;background:linear-gradient(180deg,#7fa9cf 0%,#b7cde0 45%,#9ea49a 62%,#6f7468 100%)}
.hero-title{position:absolute;left:0;top:112px;width:1200px;text-align:center;color:var(--white);font-size:47px;line-height:60px;letter-spacing:1px;text-shadow:0 2px 4px rgba(0,0,0,.25)}
.dots{position:absolute;left:570px;top:505px;display:flex;gap:7px}
.dots span{width:8px;height:8px;border-radius:50%;background:rgba(255,255,255,.7)}
.dots span.on{background:var(--white)}
.photo{position:absolute}
.price-label{position:absolute;width:260px;text-align:center}
.price-label b{display:block;font-size:16px;font-weight:700}
.price-label small{display:block;font-size:11px;color:var(--grey);margin-top:8px}
.card{position:absolute;background:var(--white);box-shadow:0 2px 14px rgba(0,0,0,.14);padding:24px 24px 0}
.card h3{font-size:17px;font-weight:500}
.card .desc{font-size:11px;color:var(--grey);margin-top:6px}
.card ul{list-style:none;margin-top:22px;border-top:1px solid var(--light)}
.card li{display:flex;justify-content:space-between;align-items:center;height:79px;border-bottom:1px solid var(--light)}
.card li:last-child{border-bottom:none}
.card li b{display:block;font-size:15px;font-weight:500}
.card li small{display:block;font-size:10.5px;color:var(--grey);margin-top:5px}
.card li .amount{font-size:22px;font-weight:700;color:var(--red)}
.field{position:absolute;background:var(--white);font-size:10px;color:#888;padding:10px 12px;text-transform:uppercase}
.info-row{position:absolute;left:757px;display:flex;gap:16px;align-items:flex-start;color:var(--white);font-size:11.5px;line-height:16px}
.info-row i{flex:none;width:28px;height:28px;border-radius:50%;background:var(--red);display:flex;align-items:center;justify-content:center}
.socials{position:absolute;left:890px;top:4240px;display:flex;gap:8px}
.socials span{width:22px;height:22px;border-radius:50%}
</style>
</head>
<body>

<header class="site-header">
  <div class="brand">
    <span class="brand-square"></span>
    <span class="brand-name">Bergungsfix<br>Talwiesen Ost</span>
  </div>
  <div class="call">
    <svg width="30" height="30" viewBox="0 0 24 24"><path fill="#1d1d1d" d="M6.6 10.8a15.1 15.1 0 0 0 6.6 6.6l2.2-2.2a1 1 0 0 1 1-.25 11.4 11.4 0 0 0 3.6.57 1 1 0 0 1 1 1V20a1 1 0 0 1-1 1A17 17 0 0 1 3 4a1 1 0 0 1 1-1h3.5a1 1 0 0 1 1 1c0 1.25.2 2.45.57 3.57a1 1 0 0 1-.25 1z"/></svg>
    <span>CALL US : 0447364891</span>
  </div>
</header>

<nav class="nav">
  <a>Home</a><a>About us</a><a>Parking Enforcement</a><a>Repossession</a><a>Breakdown Assistance</a><a>Accident Recovery</a><a>Contact</a>
</nav>

<section class="hero" role="img" aria-label="Tow truck loading a red car on an open road under a blue sky">
  <h1 class="hero-title slab">TOWING BERGFELD OST HELPS<br>IN EVERY SITUATION</h1>
  <span class="btn btn-red" style="left:432px;top:263px;width:160px;height:40px">Read more <i class="arrow"></i></span>
  <span class="btn btn-dark" style="left:606px;top:263px;width:162px;height:40px">Get started <i class="arrow"></i></span>
  <div class="dots"><span></span><span></span><span class="on"></span><span></span><span></span></div>
</section>
<svg class="abs" style="left:0;top:650px" width="1200" height="130" viewBox="0 0 1200 130">
  <polygon points="0,70 272,14 1200,125 1200,130 0,130" fill="#ffffff"/>
  <polygon points="0,70 272,14 1200,125 1200,130 272,26 0,82" fill="#e30613"/>
</svg>

<div class="photo" style="left:143px;top:822px;width:390px;height:195px;border-radius:12px;background:linear-gradient(180deg,#f3f4f6,#c9ced6)" role="img" aria-label="White tow truck with blue stripes"></div>
<h2 class="heading slab" style="left:653px;top:830px">Tow Away</h2>
<p class="lead" style="left:653px;top:895px">The costs are borne by the wrong parker</p>
<p class="copy" style="left:653px;top:922px;width:420px">Your parking space is constantly blocked by third party, wrong or long-term parkers? Act instead of getting angry! We check your parking spaces, entrances and exits, fire brigade and delivery areas and call the tow truck if necessary. We calculate the costs directly with the wrong parkers.</p>
<span class="btn btn-red" style="left:653px;top:1055px;width:128px;height:38px">Read more <i class="arrow"></i></span>
<div class="vertical" style="left:1030px;top:935px;width:220px;font-size:88px;text-align:center">TOW</div>

<svg class="abs" style="left:0;top:1085px" width="600" height="533" viewBox="0 0 600 533">
  <polygon points="0,70 170,5 600,105 600,533 0,533" fill="#e30613"/>
</svg>
<h2 class="heading slab" style="left:150px;top:1215px;color:#fff">About usTow Away</h2>
<p class="copy" style="left:150px;top:1290px;width:410px;color:#fff;font-size:12px;line-height:23px">Sed ut perspiciatis unde omnis iste natus error sit voluptatem accusantium doloremque laudantium, totam rem aperiam, eaque ipsa quae ab illo inventore veritatis et quasi architecto beatae vitae dicta sunt explicabo. Nemo enim ipsam voluptatem quia voluptas sit aspernatur aut odit aut fugit, sed quia consequuntur magni dolores</p>
<span class="btn btn-ghost" style="left:150px;top:1465px;width:128px;height:38px">Read more <i class="arrow"></i></span>
<div class="ghost-word" style="left:0;top:1528px;font-size:92px;color:rgba(255,255,255,.14)">ABOUT US</div>
<div class="photo" style="left:600px;top:1190px;width:600px;height:420px;background:linear-gradient(160deg,#8f949c,#3d434c 60%,#23272d)" role="img" aria-label="Video still of a person beside a car in front of a company banner"></div>

<h2 class="heading slab" style="left:150px;top:1755px">Free parking</h2>
<p class="lead" style="left:150px;top:1830px">Solutions for corporate and private property</p>
<p class="copy" style="left:150px;top:1858px;width:470px">We monitor your parking around the clock. We are where wrong, foreign and long-term parker problems - we solve them immediately. With our service, we ensure the satisfaction of customers, tenants, residents and employees together with you. We implement your parking conditions quickly, fairly and safely with our qualified staff. We tow if necessary immediately and take care of the entire process.</p>
<span class="btn btn-red" style="left:150px;top:2035px;width:284px;height:38px">Arrange an appointment with us <i class="arrow"></i></span>
<svg class="abs" style="left:665px;top:1710px" width="390" height="400" viewBox="0 0 390 400">
  <path d="M8,195 A187,187 0 0 0 382,195" fill="none" stroke="#e30613" stroke-width="10"/>
</svg>
<div class="photo" style="left:674px;top:1719px;width:372px;height:372px;border-radius:50%;background:radial-gradient(circle at 40% 40%,#b9b6b0,#6f6a63)" role="img" aria-label="Rows of parked cars in a car park"></div>
<div class="vertical" style="left:965px;top:1880px;width:380px;font-size:84px;text-align:center">PARKING</div>

<svg class="abs" style="left:0;top:2205px" width="1200" height="530" viewBox="0 0 1200 530">
  <polygon points="0,100 830,0 1200,85 1200,530 0,530" fill="#1b1b1b"/>
</svg>
<div class="photo" style="left:0;top:2305px;width:345px;height:422px;background:linear-gradient(180deg,#e6e6e6 0%,#e6e6e6 28%,#8a8a80 30%,#5b5a52 100%)" role="img" aria-label="Factsheet cover with a private parking sign painted on asphalt"></div>
<div class="photo" style="left:345px;top:2305px;width:255px;height:422px;background:linear-gradient(180deg,#f2f2f2 0%,#dcdcdc 62%,#9aa1aa 64%,#6d747c 100%)" role="img" aria-label="Factsheet page with printed text and a photo of parked cars"></div>
<svg class="abs" style="left:4px;top:2500px" width="28" height="32" viewBox="0 0 28 32"><rect width="28" height="32" fill="#111"/><path d="M17 9 10 16l7 7" stroke="#fff" stroke-width="2.5" fill="none"/></svg>
<svg class="abs" style="left:565px;top:2500px" width="28" height="32" viewBox="0 0 28 32"><rect width="28" height="32" fill="#111"/><path d="M11 9l7 7-7 7" stroke="#fff" stroke-width="2.5" fill="none"/></svg>
<h2 class="heading slab" style="left:682px;top:2343px;color:#fff">Factsheet Cantonal</h2>
<p class="abs" style="left:682px;top:2412px;color:#fff;font-size:17px;line-height:35px">Factsheet Regional police Bergfeld<br>Towing from private property</p>
<div class="abs" style="left:682px;top:2505px;width:373px;height:42px;background:#fff;font-size:12px;color:#333;padding:13px 14px">factsheet_abschleppen_privatgrund (pdf)</div>
<span class="btn btn-red" style="left:682px;top:2580px;width:150px;height:38px">Download
  <svg width="13" height="13" viewBox="0 0 14 14"><path d="M7 1v8M3.5 6 7 9.5 10.5 6M2 12.5h10" stroke="#fff" stroke-width="2" fill="none"/></svg></span>
<div class="ghost-word" style="left:645px;top:2648px;font-size:86px;color:rgba(255,255,255,.06)">FACTSHEET</div>

<div class="ghost-word" style="left:0;top:2780px;font-size:104px;color:#ebebeb">PRICES</div>
<h2 class="heading slab" style="left:470px;top:2818px">Transparent prices</h2>
<div class="photo" style="left:178px;top:2928px;width:188px;height:188px;border-radius:50%;background:radial-gradient(circle,#d7dde3,#8b9096);box-shadow:0 3px 0 #e30613" role="img" aria-label="Tow truck on the road"></div>
<div class="photo" style="left:507px;top:2928px;width:188px;height:188px;border-radius:50%;background:radial-gradient(circle,#c9d2dc,#6e7782);box-shadow:0 3px 0 #e30613" role="img" aria-label="Car wheel being secured for towing"></div>
<div class="photo" style="left:836px;top:2928px;width:188px;height:188px;border-radius:50%;background:radial-gradient(circle,#8d9297,#2e3236);box-shadow:0 3px 0 #e30613" role="img" aria-label="Close-up of a car rim"></div>
<div class="price-label" style="left:142px;top:3138px"><b>Empty journey Fr. 200</b><small>Empty journey only (Without any work on site)</small></div>
<div class="price-label" style="left:471px;top:3138px"><b>Towing Fr. 400</b><small>All inclusive (Car vehicles up to 2t)</small></div>
<div class="price-label" style="left:800px;top:3138px"><b>Stand costs Fr. 50</b><small>daily rate</small></div>

<div class="card" style="left:143px;top:3273px;width:444px;height:341px">
  <h3>Passenger cars up to 2t.</h3>
  <p class="desc">Add a description for this category</p>
  <ul>
    <li><div><b>Tow away</b><small>Passenger cars up to 2t.</small></div><span class="amount">400.-</span></li>
    <li><div><b>deadhead</b><small>Passenger cars up to 2t.</small></div><span class="amount">200.-</span></li>
    <li><div><b>Dri passenger cars up to 2t. article</b><small>Add a description of this item</small></div><span class="amount">22</span></li>
  </ul>
</div>
<div class="card" style="left:616px;top:3273px;width:438px;height:341px">
  <h3>Second category</h3>
  <p class="desc">Add a description for this category</p>
  <ul>
    <li><div><b>First article</b><small>Add a description of this item</small></div><span class="amount">12</span></li>
    <li><div><b>Second article</b><small>Add a description of this item</small></div><span class="amount">15</span></li>
    <li><div><b>Third article</b><small>Add a description of this item</small></div><span class="amount">22</span></li>
  </ul>
</div>

<svg class="abs" style="left:0;top:3690px" width="1200" height="606" viewBox="0 0 1200 606">
  <rect y="0" width="1200" height="606" fill="#1b1b1b"/>
  <polygon points="0,5 600,95 1200,5 1200,0 0,0" fill="#2a2a2a"/>
</svg>
<div class="vertical" style="left:960px;top:3960px;width:420px;font-size:84px;text-align:center;color:rgba(255,255,255,.05)">CONTACT</div>
<h2 class="heading slab" style="left:527px;top:3858px;color:#fff">Contact Us</h2>
<p class="abs" style="left:143px;top:3930px;color:#fff;font-size:13px;font-weight:700">Get In Touch</p>
<div class="field" style="left:143px;top:3967px;width:268px;height:30px">Name :</div>
<div class="field" style="left:420px;top:3967px;width:268px;height:30px">Phone :</div>
<div class="field" style="left:143px;top:4009px;width:545px;height:30px">Email :</div>
<div class="field" style="left:143px;top:4051px;width:545px;height:66px">Message :</div>
<span class="btn btn-red" style="left:610px;top:4133px;width:78px;height:28px;font-size:11px;border-radius:14px">Submit</span>

<p class="abs" style="left:757px;top:3930px;color:#fff;font-size:13px;font-weight:700">Contact Information</p>
<div class="info-row" style="top:3972px"><i><svg width="12" height="14" viewBox="0 0 12 14"><path d="M6 0a5 5 0 0 0-5 5c0 4 5 9 5 9s5-5 5-9a5 5 0 0 0-5-5zm0 7a2 2 0 1 1 0-4 2 2 0 0 1 0 4z" fill="#fff"/></svg></i><span>Talstrasse 24, 8155 Bergfeld,<br>Switzerland</span></div>
<div class="info-row" style="top:4022px"><i><svg width="12" height="12" viewBox="0 0 24 24"><path fill="#fff" d="M6.6 10.8a15.1 15.1 0 0 0 6.6 6.6l2.2-2.2a1 1 0 0 1 1-.25 11.4 11.4 0 0 0 3.6.57 1 1 0 0 1 1 1V20a1 1 0 0 1-1 1A17 17 0 0 1 3 4a1 1 0 0 1 1-1h3.5a1 1 0 0 1 1 1c0 1.25.2 2.45.57 3.57a1 1 0 0 1-.25 1z"/></svg></i><span style="padding-top:6px">0447364891</span></div>
<div class="info-row" style="top:4068px"><i><svg width="13" height="10" viewBox="0 0 13 10"><rect x=".5" y=".5" width="12" height="9" fill="none" stroke="#fff"/><path d="M.5.5 6.5 5.5 12.5.5" fill="none" stroke="#fff"/></svg></i><span>mail@bergungsfix.cc<br>rechnung@bergungsfix.cc</span></div>
<div class="info-row" style="top:4116px"><i><svg width="13" height="13" viewBox="0 0 14 14"><circle cx="7" cy="7" r="6" fill="none" stroke="#fff" stroke-width="1.4"/><path d="M7 3.5V7l2.5 1.5" stroke="#fff" stroke-width="1.4" fill="none"/></svg></i><span>24/7 in use for you<br>Mo. - Son. 24h</span></div>

<div class="abs" style="left:143px;top:4225px;width:914px;height:1px;background:#333"></div>
<p class="abs" style="left:143px;top:4246px;color:#ccc;font-size:11px">Copyrights © 2015, Companyname. All Rights Reserved. &nbsp;|&nbsp; Privacy policy</p>
<div class="socials"><span style="background:#3b5a98"></span><span style="background:#2aa3ef"></span><span style="background:#d9342a"></span><span style="background:#b07a4a"></span><span style="background:#1e7bb8"></span></div>

</body>
</html>
```